Landscape Construction and Design Company

We are a landscape construction and design company from New Jersey. We design and install landscapes and hardscapes for residential properties. The name of the company is Brevin's Landscape and Design LLC. We specialize mostly in planting trees and stone work, some water features. We would like to see design themes that include a tree or trees and a stone walkway or wall. We like earth tone colors. We like traditional to modern designs.

Target Market(s)

Homeowners

Industry/Entity Type

Landscape

Contact Information for Business Card

Nature themed design, earth tone colors, space for company name, address, phone numbers, email and website address

Logo Text

No text

Font styles to use
Serif

Colors

Designer to choose colors to be used in the design.

Requirements
Must have
• A tree or trees, similar to the ones uploaded in my supporting images
Nice to have
• I like trees similar to those in my uploaded supporting images. I like artistic, nature theme, earth tone colors
Should not have
• Pictures of real landscapes, cartoon looking logo or objects

```html
<!DOCTYPE html>
<html lang="en">
<head>
<meta charset="utf-8">
<title>Brevin's Landscape and Design LLC – Business Card</title>
<link href="https://fonts.googleapis.com/css2?family=Cinzel:wght@700&family=Lato:wght@400;700&display=swap" rel="stylesheet">
<style>
  :root {
    --backdrop: #4a413b;
    --card: #111111;
    --leaf-green: #7cc242;
    --silver: #cfcfcf;
    --text-light: #f2f2f2;
    --divider: #3a3a3a;
  }
  * { box-sizing: border-box; margin: 0; padding: 0; }
  html, body { width: 1200px; height: 900px; overflow: hidden; }
  body {
    background: var(--backdrop);
    display: flex;
    align-items: center;
    justify-content: center;
    gap: 40px;
    font-family: "Lato", sans-serif;
  }
  .card {
    width: 540px;
    height: 310px;
    background: var(--card);
    position: relative;
    box-shadow: 0 10px 30px rgba(0,0,0,0.45);
  }

  /* Shared brand mark: plain dot + name in the text font */
  .brand-dot {
    width: 60px; height: 60px;
    border-radius: 50%;
    background: var(--leaf-green);
    flex: none;
  }
  .brand-name {
    font-family: "Lato", sans-serif;
    font-weight: 400;
    color: var(--leaf-green);
    white-space: nowrap;
  }

  /* Front: contact side */
  .card-front { display: flex; }
  .front-brand {
    width: 300px;
    display: flex;
    flex-direction: column;
    align-items: center;
    justify-content: center;
    gap: 18px;
  }
  .front-brand .brand-name { font-size: 16px; }
  .front-divider {
    width: 1px;
    background: var(--divider);
    margin: 40px 0;
  }
  .contact {
    flex: 1;
    padding: 46px 0 0 22px;
    color: var(--text-light);
    font-size: 15px;
  }
  .contact-name {
    font-family: "Cinzel", serif;
    font-weight: 700;
    color: var(--leaf-green);
    font-size: 18px;
    letter-spacing: 0.5px;
  }
  .contact-role { margin-bottom: 10px; }
  .contact-list { list-style: none; }
  .contact-list li {
    display: flex;
    align-items: center;
    gap: 8px;
    line-height: 1.5;
  }
  .contact-list svg { width: 11px; height: 11px; fill: var(--leaf-green); flex: none; }
  .contact-address { margin-top: 12px; line-height: 1.35; }

  /* Back: brand side */
  .card-back {
    display: flex;
    flex-direction: column;
    align-items: center;
    justify-content: center;
    gap: 40px;
  }
  .back-brand {
    display: flex;
    align-items: center;
    gap: 16px;
  }
  .back-brand .brand-dot { background: var(--silver); width: 48px; height: 48px; }
  .back-brand .brand-name { color: var(--silver); font-size: 20px; }
  .services {
    font-size: 14px;
    letter-spacing: 0.5px;
    color: var(--silver);
  }
  .services .bar { color: var(--leaf-green); padding: 0 4px; }
</style>
</head>
<body>
  <section class="card card-front">
    <div class="front-brand">
      <span class="brand-dot"></span>
      <p class="brand-name">Brevin's Landscape and Design LLC</p>
    </div>
    <div class="front-divider"></div>
    <div class="contact">
      <p class="contact-name">MARCUS HALE</p>
      <p class="contact-role">Managing Director</p>
      <ul class="contact-list">
        <li><svg viewBox="0 0 12 12"><path d="M2.5 0.5l2 2.5-1 1.3c0.7 1.5 1.8 2.6 3.3 3.3l1.3-1 2.5 2-1.2 2.2C5.2 10.5 1.5 6.8 0.3 1.7z"/></svg>444 555 0192</li>
        <li><svg viewBox="0 0 12 12"><path d="M0 2h12v8H0z M0.8 2.5L6 6.5l5.2-4" stroke="#111" stroke-width="0.9"/></svg>hello@brevinsland.com</li>
        <li><svg viewBox="0 0 12 12"><circle cx="6" cy="6" r="5.5"/></svg>www.brevinsland.com</li>
      </ul>
      <p class="contact-address">18 Maple Row,<br>Trenton, NJ 08608</p>
    </div>
  </section>

  <section class="card card-back">
    <div class="back-brand">
      <span class="brand-dot"></span>
      <p class="brand-name">Brevin's Landscape and Design LLC</p>
    </div>
    <p class="services">PLANTING TREES<span class="bar">|</span>STONE WORK<span class="bar">|</span>WATER FEATURES</p>
  </section>
</body>
</html>
```